Website for Youth Orchestra to sell tickets and attract young musicians

We are looking for a new website design for a Youth Orchestra; one of the best classical youth orchestras in the county. This project is the design only. <br/><br/>The website serves two main purposes:<br/>• Selling tickets for concerts and performances of the orchestra<br/>• Recruiting young musicians to do audition for the orchestra<br/>
Updates

Target Market(s)

Classical music lovers with a special interest in young upcoming musicians.
Young talented musicians

Number of Pages Required

2 page

Colors
ec1f27

Requirements
Must have
• - A Picture on the front page that promotes the main upcomming event
• - Attention for recruiting new musicians
• - Pictures with young musicians (white back ground, see examples)
• - Responsive
• - Please use the logo attached
Should not have
• The brown colors of the current website (kvb-veldhorst.example)

```html
<!DOCTYPE html>
<html lang="nl">
<head>
<meta charset="utf-8">
<title>Veldhorst Jeugd Orkest</title>
<link rel="stylesheet" href="https://fonts.googleapis.com/css2?family=Poppins:wght@300;400;500;600&family=Raleway:wght@300;400&family=Playball&display=swap">
<style>
:root{
  --red:#ec1f27;
  --black:#0b0b0b;
  --text:#3a3a3a;
  --muted:#777;
  --cream:#f6f3e8;
  --pink:#fce8ea;
  --white:#fff;
  --line:#e6e6e6;
}
*{box-sizing:border-box;margin:0;padding:0}
html,body{width:1200px;height:4367px;overflow:hidden}
body{font-family:"Poppins",sans-serif;color:var(--text);background:var(--white);position:relative}
.abs{position:absolute}
.btn{display:inline-flex;align-items:center;justify-content:center;gap:6px;border-radius:20px;font-size:13px;font-weight:500;text-decoration:none}
.btn-red{background:var(--red);color:var(--white)}
.btn-line{border:1.5px solid var(--red);color:var(--red);background:var(--white)}
.heading{font-family:"Raleway",sans-serif;font-weight:300;color:#222;font-size:36px}
.divider{display:flex;align-items:center;justify-content:center;gap:8px}
.divider span{width:70px;height:1px;background:#ccc}
.divider i{width:10px;height:10px;border-radius:50%;background:var(--red);display:block}
p{line-height:1.9}

/* top bar */
.topbar{top:0;left:0;width:1200px;height:46px;background:var(--white)}
.mail{left:141px;top:8px;display:flex;align-items:center;gap:10px;font-size:13px;color:#222}
.mail b{width:30px;height:30px;border-radius:50%;background:var(--red);display:flex;align-items:center;justify-content:center}
.top-actions{right:141px;top:7px;display:flex;gap:8px}
.top-actions .btn{height:30px;padding:0 16px;font-size:12px}
.nav{top:46px;left:0;width:1200px;height:39px;background:var(--red)}
.nav a{position:absolute;top:13px;color:var(--white);font-size:11px;font-weight:500;text-decoration:none}
.logo{left:494px;top:-106px;width:212px;height:212px;border-radius:50%;background:var(--red);z-index:3;display:flex;align-items:flex-end;justify-content:center;padding-bottom:30px}
.logo span{color:var(--white);font-family:"Poppins",sans-serif;font-weight:500;font-size:17px;line-height:1.1;text-align:center}

/* hero */
.hero{top:85px;left:0;width:1200px;height:486px;background:var(--black)}
.hero-photo{right:0;top:0;width:620px;height:486px;background:radial-gradient(ellipse at 60% 45%,#5a4a3e 0%,#2a211c 45%,#0b0b0b 80%)}
.welcome{left:141px;top:95px;font-family:"Playball",cursive;color:var(--red);font-size:34px}
.hero-title{left:141px;top:130px;font-family:"Playball",cursive;font-weight:400;color:var(--white);font-size:54px;line-height:68px}
.hero-text{left:141px;top:265px;width:420px;color:var(--white);font-size:14px;line-height:21px}
.hero .btn{left:141px;top:353px;height:34px;padding:0 16px;position:absolute}

/* about */
.about-photo{left:142px;top:641px;width:431px;height:431px;border-radius:50%;background:radial-gradient(circle at 45% 40%,#e8e2dc,#a68c76 60%,#5b4636)}
.about{left:628px;top:650px;width:432px}
.about h2{margin-bottom:14px}
.about h4{font-size:13px;font-weight:600;color:#222;margin:22px 0 10px}
.about p{font-size:11.5px;color:#555;margin-bottom:8px}
.about .btn{height:34px;padding:0 22px;margin-top:14px}

/* shows */
.shows{top:1144px;left:0;width:1200px;height:580px;background:var(--cream)}
.shows .heading{position:absolute;top:58px;width:1200px;text-align:center}
.shows .divider{position:absolute;top:122px;width:1200px}
.events{left:141px;top:164px;width:918px;background:var(--white);box-shadow:0 2px 8px rgba(0,0,0,.06)}
.events-head{height:46px;display:flex;font-size:12px;font-weight:500;color:#333;border-bottom:1px solid var(--line)}
.events-head div{flex:1;display:flex;align-items:center;justify-content:center;gap:6px}
.event{height:75px;display:flex;align-items:center;border-bottom:1px solid var(--line);font-size:11px;position:relative;background:var(--white)}
.event.raised{box-shadow:0 4px 14px rgba(0,0,0,.14);z-index:2;margin:0 -6px;padding:0 6px}
.date{width:78px;text-align:center;line-height:1.35;font-size:10px;color:#333;border-right:1px solid var(--line);padding:4px 0}
.date b{display:block;font-size:12px}
.ev-title{margin-left:24px;width:440px;color:#666;font-size:10.5px;line-height:1.5}
.ev-title b{display:block;color:#222;font-weight:500;font-size:12px}
.ev-meta{display:flex;align-items:center;gap:6px;color:#666;width:130px}
.ev-time{width:110px}
.event .btn{height:28px;width:98px;font-size:11px;font-weight:600}
.view-all{left:541px;top:472px;width:118px;height:34px;position:absolute}

/* musicians */
.musicians .heading{position:absolute;top:1785px;width:1200px;text-align:center}
.musicians .divider{top:1849px;left:0;width:1200px;position:absolute}
.card{top:1883px;width:212px;height:309px;background:var(--white);box-shadow:0 3px 10px rgba(0,0,0,.1);text-align:center}
.card .ph{height:245px}
.card h5{font-size:14px;font-weight:600;color:#222;margin-top:12px}
.card small{font-size:12px;color:#555}

/* missie */
.mv-title{top:2262px;width:1200px;text-align:center}
.mv-div{top:2325px;left:0;width:1200px}
.mv-card{left:141px;top:2370px;width:918px;height:303px;background:var(--white);box-shadow:0 3px 18px rgba(0,0,0,.1);display:flex}
.mv-col{flex:1;padding:40px 36px 0;text-align:center}
.mv-col+.mv-col{border-left:1px dashed #ddd}
.mv-col h5{font-size:16px;font-weight:500;color:#222;margin:14px 0 12px}
.mv-col p{font-size:11.5px;color:#555}
.mv-logo{left:514px;top:2362px;width:172px;height:80px;border-radius:0 0 86px 86px;background:var(--red);display:flex;align-items:center;justify-content:center;z-index:2}
.mv-logo span{color:var(--white);font-weight:500;font-size:14px;line-height:1.1;text-align:center}
.mv-btn{left:539px;top:2709px;width:122px;height:34px;position:absolute}

/* tickets */
.tk-title{top:2805px;width:1200px;text-align:center}
.tk-div{top:2868px;left:0;width:1200px}
.tk-text{top:2895px;width:1200px;text-align:center;font-size:12px;color:#555}
.tk-bold{top:2923px;width:1200px;text-align:center;font-size:12px;font-weight:500;color:#222}
.ticket{left:505px;top:2963px;width:190px;height:83px;background:linear-gradient(90deg,#222 0 14px,#f1ead3 14px 176px,#222 176px)}

/* career */
.career{top:3119px;left:0;width:1200px;height:475px;background:var(--pink);overflow:hidden}
.career .circle{border-radius:50%;background:#f6c9cd}
.career-photo{left:644px;top:60px;width:400px;height:415px;background:linear-gradient(180deg,#d9b38f 0%,#3a2c26 40%,#0d0d0d 100%)}
.career h2{left:141px;top:130px;position:absolute}
.career .divider{left:141px;top:190px;position:absolute;justify-content:flex-start}
.career p{left:141px;top:220px;width:420px;position:absolute;font-size:12px;color:#555}
.career .btn{left:141px;top:322px;height:34px;width:100px;position:absolute}

/* newsletter */
.nl-title{left:200px;top:3700px;width:260px;text-align:right;line-height:46px}
.nl-rule{left:482px;top:3680px;width:1px;height:150px;background:#ddd}
.nl-text{left:516px;top:3716px;font-size:12px;font-weight:500;color:#222}
.nl-form{left:516px;top:3748px;width:452px;height:40px;display:flex;border-radius:20px;overflow:hidden;border:1px solid #ddd}
.nl-form span{flex:1;padding-left:16px;font-size:11px;color:#aaa;display:flex;align-items:center}
.nl-form b{width:110px;background:var(--red);color:var(--white);font-size:13px;font-weight:500;display:flex;align-items:center;justify-content:center}

/* footer */
.footer{top:3899px;left:0;width:1200px;height:423px;background:var(--black);color:var(--white)}
.fcol{top:70px}
.fcol h6{font-size:16px;font-weight:500;margin-bottom:18px}
.fcol li{list-style:none;font-size:12px;line-height:26.7px;color:#ddd}
.fsep{top:80px;width:0;height:260px;border-left:1px dashed #555}
.contact li{display:flex;gap:10px;line-height:20px;margin-bottom:10px}
.badge{width:96px;height:66px;background:var(--white);border-radius:2px}
.bottom{top:4322px;left:0;width:1200px;height:45px;background:var(--red);color:var(--white)}
.bottom small{position:absolute;left:141px;top:14px;font-size:11px}
.social{position:absolute;right:141px;top:11px;display:flex;gap:6px}
.social i{width:23px;height:23px;border-radius:50%;background:var(--white);display:block}
</style>
</head>
<body>

<header>
  <div class="abs topbar"></div>
  <div class="abs mail"><b><svg width="13" height="10" viewBox="0 0 13 10"><rect x="0.5" y="0.5" width="12" height="9" fill="none" stroke="#fff"/><path d="M1 1l5.5 4.5L12 1" fill="none" stroke="#fff"/></svg></b>info@veldhorstorkest.example</div>
  <div class="abs top-actions">
    <a class="btn btn-line"><svg width="14" height="10" viewBox="0 0 14 10"><rect x="1" y="1" width="12" height="8" rx="1" fill="none" stroke="#ec1f27" stroke-width="1.4"/><path d="M5 1v8" stroke="#ec1f27" stroke-dasharray="1.5 1.5"/></svg>Koop Kaartjes</a>
    <a class="btn btn-red"><svg width="12" height="12" viewBox="0 0 12 12"><path d="M1 6h7M5 3l3 3-3 3M8 1h3v10H8" fill="none" stroke="#fff" stroke-width="1.4"/></svg>Log In</a>
  </div>
  <nav class="abs nav">
    <a style="left:148px">Home</a><a style="left:206px">Orkest</a><a style="left:271px">Speel Mee</a><a style="left:354px">Concerten</a><a style="left:437px">Tournees</a>
    <a style="left:715px">Partners</a><a style="left:786px">Vrienden</a><a style="left:858px">Oudleden</a><a style="left:943px">Contact &amp; Organisatie</a>
  </nav>
  <div class="abs logo"><span>Veldhorst<br>Jeugd Orkest</span></div>
</header>

<section class="abs hero">
  <div class="abs hero-photo" role="img" aria-label="Photo of a young violinist playing, on a dark background with music notes"></div>
  <div class="abs welcome">Welkom Bij</div>
  <h1 class="abs hero-title">Veldhorst<br>Tickets Music</h1>
  <p class="abs hero-text">Het VJO is opgericht in 1962 door twaalf kinderen van de Veldhorster muziekschool en stond vijfentwintig jaar lang onder leiding van Jan van Dijkhof.</p>
  <a class="btn btn-red"><svg width="14" height="10" viewBox="0 0 14 10"><rect x="1" y="1" width="12" height="8" rx="1" fill="none" stroke="#fff" stroke-width="1.4"/></svg>Koop Kaartjes</a>
</section>

<section>
  <div class="abs about-photo" role="img" aria-label="Round photo of a young woman playing the violin"></div>
  <div class="abs about">
    <h2 class="heading">Over VJO</h2>
    <div class="divider" style="justify-content:flex-start;margin-top:8px"><i></i><span style="width:40px"></span></div>
    <h4>Het Veldhorst Jeugd Orkest speelt vol vuur!</h4>
    <p>Het Veldhorst Jeugd Orkest (VJO) is een jeugdorkest dat speelt in volledig symfonische bezetting. Het orkest telt circa zeventig jonge musici uit Veldhorst en omstreken, in de leeftijd van dertien tot vierentwintig jaar. De musici zijn merendeels middelbare scholieren en studenten. Het orkest repeteert iedere vrijdagavond in de Lindenhofkerk in Veldhorst. Deze repetitie is openbaar toegankelijk. Wie wil komen luisteren, is welkom!</p>
    <p>Het VJO is opgericht in 1962 door twaalf kinderen van de Veldhorster muziekschool en stond vijfentwintig jaar lang onder leiding van Jan van Dijkhof. Van 1987 tot aan 2005 was Karel Mertens.</p>
    <a class="btn btn-red">Lees Verder</a>
  </div>
</section>

<section class="abs shows">
  <h2 class="heading">Upcoming Shows</h2>
  <div class="divider"><span></span><i></i><span></span></div>
  <div class="abs events">
    <div class="events-head">
      <div><svg width="10" height="13" viewBox="0 0 10 13"><path d="M5 12S1 7 1 4.5a4 4 0 018 0C9 7 5 12 5 12z" fill="#ec1f27"/></svg>Events Near All Location</div>
      <div><svg width="12" height="10" viewBox="0 0 12 10"><path d="M0 1h12M0 5h12M0 9h12" stroke="#ec1f27" stroke-width="1.5"/></svg>Filters</div>
    </div>
    <div class="event"><div class="date">Fri<b>JAN 31</b>7:00 pm</div><div class="ev-title"><b>Lorem ipsum dolor sit amet</b>Consectetuer adipiscing elit</div><div class="ev-meta"><svg width="9" height="12" viewBox="0 0 10 13"><path d="M5 12S1 7 1 4.5a4 4 0 018 0C9 7 5 12 5 12z" fill="#ec1f27"/></svg>Lorem ipsum dolor</div><div class="ev-meta ev-time"><svg width="12" height="12" viewBox="0 0 12 12"><circle cx="6" cy="6" r="5" fill="none" stroke="#ec1f27"/><path d="M6 3v3h2" fill="none" stroke="#ec1f27"/></svg>8:00 pm</div><a class="btn btn-red">TICKETS</a></div>
    <div class="event raised"><div class="date">Sat<b>FEB 1</b>10:00 am</div><div class="ev-title"><b>Lorem ipsum dolor sit amet</b>Consectetuer adipiscing elit</div><div class="ev-meta"><svg width="9" height="12" viewBox="0 0 10 13"><path d="M5 12S1 7 1 4.5a4 4 0 018 0C9 7 5 12 5 12z" fill="#ec1f27"/></svg>Lorem ipsum dolor</div><div class="ev-meta ev-time"><svg width="12" height="12" viewBox="0 0 12 12"><circle cx="6" cy="6" r="5" fill="none" stroke="#ec1f27"/><path d="M6 3v3h2" fill="none" stroke="#ec1f27"/></svg>8:00 pm</div><a class="btn btn-red">TICKETS</a></div>
    <div class="event" style="border-bottom:0"><div class="date">Wed<b>FEB 4</b>12:00 am</div><div class="ev-title"><b>Lorem ipsum dolor sit amet</b>Consectetuer adipiscing elit</div><div class="ev-meta"><svg width="9" height="12" viewBox="0 0 10 13"><path d="M5 12S1 7 1 4.5a4 4 0 018 0C9 7 5 12 5 12z" fill="#ec1f27"/></svg>Lorem ipsum dolor</div><div class="ev-meta ev-time"><svg width="12" height="12" viewBox="0 0 12 12"><circle cx="6" cy="6" r="5" fill="none" stroke="#ec1f27"/><path d="M6 3v3h2" fill="none" stroke="#ec1f27"/></svg>8:00 pm</div><a class="btn btn-red">TICKETS</a></div>
  </div>
  <a class="btn btn-line view-all">View All</a>
</section>

<section class="musicians">
  <h2 class="heading">Musicians</h2>
  <div class="divider"><span></span><i></i><span></span></div>
  <div class="abs card" style="left:171px"><div class="ph" role="img" aria-label="Photo of a cellist in a dark suit" style="background:linear-gradient(90deg,#e9ecef,#c7ccd2 50%,#3b3230)"></div><h5>Elias Verbeek</h5><small>Klarinet</small></div>
  <div class="abs card" style="left:407px"><div class="ph" role="img" aria-label="Photo of a young man playing the tuba" style="background:linear-gradient(180deg,#b9a88e,#8e7a5a 60%,#d2b87a)"></div><h5>Joris Dammers</h5><small>Altviool</small></div>
  <div class="abs card" style="left:642px"><div class="ph" role="img" aria-label="Photo of a young woman playing the violin" style="background:linear-gradient(135deg,#e6a53a,#8a4a1a 55%,#2a1a12)"></div><h5>Marit Vos</h5><small>Hobo</small></div>
  <div class="abs card" style="left:878px"><div class="ph" role="img" aria-label="Photo of a young man in a suit playing the violin" style="background:linear-gradient(180deg,#efe3d6,#c9b39c 50%,#2a2420)"></div><h5>Jonas de Wit</h5><small>Slagwerk</small></div>
</section>

<section>
  <h2 class="abs heading mv-title">Missie, Visie &amp; Solisten</h2>
  <div class="abs divider mv-div"><span></span><i></i><span></span></div>
  <div class="abs mv-card">
    <div class="mv-col">
      <svg width="58" height="58" viewBox="0 0 58 58"><circle cx="27" cy="31" r="24" fill="none" stroke="#ec1f27" stroke-width="3"/><circle cx="27" cy="31" r="15" fill="none" stroke="#ec1f27" stroke-width="3"/><circle cx="27" cy="31" r="6" fill="#ec1f27"/><path d="M27 31L50 8M44 6l6 2 2 6" fill="none" stroke="#ec1f27" stroke-width="3"/></svg>
      <h5>Missie</h5>
      <p>Het Veldhorst Jeugd Orkest (VJO) wil voor de jeugd uit Veldhorst en omstreken een uitdagend podium zijn, waarop zij haar muzikale talent volledig tot bloei kan laten komen.</p>
    </div>
    <div class="mv-col">
      <svg width="62" height="58" viewBox="0 0 62 58"><path d="M2 29C12 14 22 9 31 9s19 5 29 20C50 44 40 49 31 49S12 44 2 29z" fill="none" stroke="#ec1f27" stroke-width="3"/><circle cx="31" cy="29" r="10" fill="none" stroke="#ec1f27" stroke-width="3"/><circle cx="31" cy="29" r="4" fill="#ec1f27"/></svg>
      <h5>Visie</h5>
      <p>Het VJO wil een zo breed mogelijk publiek bereiken door prikkelende symfonische programma's samen te stellen. We nodigen daarbij graag andere kunstdisciplines uit zoals bijvoorbeeld bij onze educatievoorstellingen. Denk daarbij ook aan het ten gehore brengen van (nieuwe) composities uit andere muziekgenres zoals pop, jazz, tango &amp; klezmer. Voorbeelden daarvan ziet u bij partners in muziek.</p>
    </div>
  </div>
  <div class="abs mv-logo"><span>Veldhorst<br>Jeugd Orkest</span></div>
  <a class="btn btn-red mv-btn">Lees Verder</a>
</section>

<section>
  <h2 class="abs heading tk-title">Online Kaarten Bestellen</h2>
  <div class="abs divider tk-div"><span></span><i></i><span></span></div>
  <p class="abs tk-text">Het orkest geeft meerdere concerten per jaar en verkoopt online tickets om hun activiteiten te financieren.</p>
  <p class="abs tk-bold">Ga direct naar onze bestelpagina</p>
  <div class="abs ticket" role="img" aria-label="Illustrated concert ticket with date and price"></div>
</section>

<section class="abs career">
  <div class="abs circle" style="left:560px;top:30px;width:150px;height:150px"></div>
  <div class="abs circle" style="left:940px;top:225px;width:165px;height:165px"></div>
  <div class="abs career-photo" role="img" aria-label="Photo of a young woman in black playing the violin"></div>
  <h2 class="heading">Musical Career</h2>
  <div class="divider"><i></i><span style="width:40px"></span></div>
  <p>Een orkest met jonge mensen die zeer getalenteerd zijn. De meeste zijn voorbestemd of studeren al aan het conservatorium van muziek. Het orkest trekt jonge muzikanten uit andere orkesten aan die een volgende stap in hun muzikale carrière willen nemen.</p>
  <a class="btn btn-red">join now</a>
</section>

<section>
  <h2 class="abs heading nl-title">Nieuwsbrief Inschrijven</h2>
  <div class="abs nl-rule"></div>
  <p class="abs nl-text">Abonneer u op onze nieuwsbrief voor de nieuwste update in uw inbox</p>
  <div class="abs nl-form"><span>Vul je e-mailadres in</span><b>Abonneren</b></div>
</section>

<footer class="abs footer">
  <div class="abs fcol" style="left:141px"><h6>Snelle links</h6><ul><li>Huis</li><li>Orkest</li><li>Speel Mee</li><li>Concerten</li><li>Tournees</li><li>Partners</li><li>Vrienden</li><li>Oudleden</li><li>Contact &amp; Organisatie</li></ul></div>
  <div class="abs fsep" style="left:384px"></div>
  <div class="abs fcol" style="left:503px"><h6>Andere links</h6><ul><li>Commissies</li><li>Dirigent</li><li>gedragscode</li><li>Orkestleden</li><li>Auditiedata</li><li>Auditieformulier</li><li>Repetitie Bezoeken</li><li>Vacatures</li><li>Bestuur</li><li>Word Vriend</li></ul></div>
  <div class="abs fsep" style="left:730px"></div>
  <div class="abs fcol contact" style="left:849px"><h6>Contact details</h6>
    <ul>
      <li><svg width="12" height="16" viewBox="0 0 10 13"><path d="M5 12S1 7 1 4.5a4 4 0 018 0C9 7 5 12 5 12z" fill="#ec1f27"/></svg><span><b style="font-weight:500">Veldhorst Tickets Music</b><br>Veldhorst Youth Orchestra<br>Postbus 412, 7400LK Veldhorst</span></li>
      <li><svg width="12" height="12" viewBox="0 0 12 12"><path d="M2 1l3 1-1 3 3 3 3-1 1 3-2 1C6 11 1 6 1 3z" fill="#ec1f27"/></svg><span style="color:#666">055 123 4589</span></li>
      <li><svg width="13" height="10" viewBox="0 0 13 10"><rect width="13" height="10" fill="#ec1f27"/><path d="M0.5 0.5l6 5 6-5" fill="none" stroke="#000"/></svg>info@kvb-veldhorst.example</li>
    </ul>
    <h6 style="margin-top:20px">Onze Partners</h6>
    <div style="display:flex;gap:8px"><div class="badge" role="img" aria-label="Partner badge"></div><div class="badge" role="img" aria-label="Certification badge"></div></div>
  </div>
</footer>
<div class="abs bottom"><small>© 2020 Veldhorst Jeugd Orkest. All Rights Reserved.</small><div class="social"><i></i><i></i><i></i></div></div>

</body>
</html>
```